Need a flyer to leave behind when visiting clients or at shows

Glossy colorful tri-fold flyer with the same information that is on my web site www.brevalinkpro.com. I am open to a little modern or creative take on the typical brochure. I created the web site so I can provide any raw files needed from it. I would also like the ability to edit this flyer in the future in Adobe Photoshop Elements

```html
<!DOCTYPE html>
<html lang="en">
<head>
<meta charset="utf-8">
<title>BrevaLink Healthcare Solutions – Tri-fold Cover</title>
<link rel="stylesheet" href="https://fonts.googleapis.com/css2?family=Montserrat:wght@400;500;700&display=swap">
<style>
  :root {
    --backdrop: #9e9e9e;
    --purple-light: #6a3c98;
    --purple-deep: #5a2688;
    --photo-warm: #e9cdbd;
    --photo-soft: #f3e8e3;
    --photo-mid: #d8c3b6;
    --white: #ffffff;
  }
  * { box-sizing: border-box; margin: 0; padding: 0; }
  html, body {
    width: 1200px;
    height: 800px;
    overflow: hidden;
  }
  body {
    background: var(--backdrop);
    display: flex;
    align-items: center;
    justify-content: center;
    font-family: "Montserrat", Arial, sans-serif;
  }
  .cover-panel {
    width: 318px;
    height: 736px;
    display: flex;
    flex-direction: column;
    box-shadow: 0 10px 30px rgba(0,0,0,0.25);
    background: var(--white);
  }
  .cover-photo {
    flex: 0 0 58%;
    background: linear-gradient(160deg, var(--photo-warm) 0%, var(--photo-soft) 45%, var(--photo-mid) 75%, var(--photo-soft) 100%);
  }
  .cover-band {
    flex: 1;
    background: linear-gradient(180deg, var(--purple-light) 0%, var(--purple-deep) 100%);
    color: var(--white);
    display: flex;
    flex-direction: column;
    align-items: center;
    padding: 44px 24px 0;
    text-align: center;
  }
  .brand-name {
    font-weight: 700;
    font-size: 30px;
    letter-spacing: -0.5px;
    line-height: 1;
  }
  .brand-tagline {
    font-weight: 700;
    font-size: 9px;
    letter-spacing: 1.2px;
    margin-top: 6px;
    text-transform: uppercase;
  }
  .cover-headline {
    margin-top: 44px;
    font-weight: 700;
    font-size: 19px;
    line-height: 1.3;
  }
</style>
</head>
<body>
  <main class="cover-panel">
    <div class="cover-photo" role="img" aria-label="Soft-focus photo of a bright clinic reception desk with flowers, overlaid with a white hexagon pattern"></div>
    <section class="cover-band">
      <p class="brand-name">BrevaLink</p>
      <p class="brand-tagline">Healthcare Solutions</p>
      <h1 class="cover-headline">Increasing The Value<br>and Security of Your<br>Technology Resources</h1>
    </section>
  </main>
</body>
</html>
```